6"x9" Postcard Mailer

A 6"x9" Postcard mailer targeted to forensic laboratories to advertise or mock forensic samples (https://veltrascience.example/products/trial-lab-specimens/).

Here is some copy, but we can modify if there is not enough space:

Headline:
Expedite Training, Validation, & R&D with Our Ready-to-Use Mock Samples

Bullet Points:

- Wide Variety of Sample Types: IRB-approved samples mimicking crime scene substances, including semen, hair, bone, saliva, blood, and vaginal epithelial cells.
- Diverse Scenarios: Simulate sexual assault and degraded samples for varied conditions.
- Custom Solutions: Tailored DNA quantities and concentrations to suit your lab's needs.

Use discount code PRAX47 for a 10% discount

```html
<!DOCTYPE html>
<html lang="en">
<head>
<meta charset="utf-8">
<title>Veltra Science – Trial Lab Specimens Postcard</title>
<link rel="stylesheet" href="https://fonts.googleapis.com/css2?family=Poppins:wght@400;500;600;800;900&display=swap">
<style>
  :root{
    --bg:#23272f;
    --paper:#ffffff;
    --navy:#1f4ea5;
    --sky:#2690d0;
    --ink:#111111;
    --photo-dark:#0d1630;
    --photo-mid:#2c56c4;
    --photo-light:#e9e9ee;
  }
  *{margin:0;padding:0;box-sizing:border-box;}
  html,body{width:1200px;height:2726px;overflow:hidden;background:var(--bg);}
  body{position:relative;font-family:"Poppins",sans-serif;}
  .card{position:absolute;left:206px;width:768px;height:546px;background:var(--paper);overflow:hidden;}
  .card--front{top:1289px;}
  .card--back{top:1889px;height:543px;}
  .card svg.shapes{position:absolute;inset:0;width:100%;height:100%;}
  .headline{position:absolute;left:59px;top:67px;color:var(--navy);font-weight:900;font-size:34px;line-height:35px;letter-spacing:.2px;text-transform:uppercase;}
  .subhead{position:absolute;left:59px;top:203px;color:var(--ink);font-weight:500;font-size:29px;line-height:29px;}
  .offer-percent{position:absolute;left:59px;top:318px;color:var(--sky);font-weight:900;font-size:68px;line-height:68px;letter-spacing:-1px;}
  .offer-label{position:absolute;left:68px;top:386px;color:var(--ink);font-weight:500;font-size:29px;line-height:30px;}
  .code-intro{position:absolute;left:214px;top:334px;color:var(--ink);font-size:30px;line-height:30px;}
  .code-box{position:absolute;left:214px;top:370px;width:220px;height:44px;border:2px solid var(--sky);color:var(--sky);font-weight:800;font-size:29px;line-height:40px;padding-left:8px;}
  .brand{position:absolute;color:var(--navy);font-weight:500;font-size:40px;line-height:44px;letter-spacing:-.5px;}
  .card--front .brand{left:59px;top:435px;}
  .card--back .brand{left:426px;top:430px;}
  .web{position:absolute;right:60px;color:#fff;font-size:16px;line-height:20px;}
  .card--front .web{top:516px;}
  .card--back .web{top:512px;}
  .features{position:absolute;left:59px;top:99px;width:310px;color:#fff;list-style:none;}
  .features li{font-size:17px;line-height:19px;margin-bottom:24px;}
  .features strong{display:block;font-weight:800;font-size:20px;line-height:20px;}
  .stamp{position:absolute;left:591px;top:63px;width:118px;height:137px;border:1px solid #8a8a8a;}
  .address-line{position:absolute;left:431px;width:265px;height:1px;background:#8a8a8a;}
</style>
</head>
<body>

<section class="card card--front" aria-label="Postcard front">
  <svg class="shapes" viewBox="0 0 768 546" aria-hidden="true">
    <defs>
      <linearGradient id="photoTone" x1="0" y1="0" x2="1" y2="1">
        <stop offset="0" stop-color="var(--photo-dark)"/>
        <stop offset=".45" stop-color="var(--photo-mid)"/>
        <stop offset="1" stop-color="var(--photo-light)"/>
      </linearGradient>
    </defs>
    <line x1="420" y1="412" x2="470" y2="412" stroke="var(--sky)" stroke-width="2"/>
    <path d="M300 546 C360 546 352 505 420 505 L768 505 L768 546 Z" fill="var(--navy)"/>
    <rect x="0" y="540" width="768" height="6" fill="var(--navy)"/>
  </svg>
  <svg class="shapes" viewBox="0 0 768 546" role="img" aria-label="Photo: gloved hands in blue nitrile lifting a red-capped swab from a blood spatter on a white surface">
    <path d="M500 0 C340 40 280 250 350 380 C410 470 560 485 768 455 L768 0 Z" fill="url(#photoTone)"/>
  </svg>

  <h1 class="headline">Expedite<br>Training,<br>Validation,<br>&amp; R&amp;D</h1>
  <p class="subhead">with Our-Ready<br>to-Use Mock<br>Samples</p>
  <p class="offer-percent">10%</p>
  <p class="offer-label">discount</p>
  <p class="code-intro">Use code</p>
  <p class="code-box">PRAX47</p>
  <p class="brand">Veltra Science</p>
  <p class="web">www.veltrascience.example</p>
</section>

<section class="card card--back" aria-label="Postcard back">
  <svg class="shapes" viewBox="0 0 768 543" aria-hidden="true">
    <path d="M0 0 L200 0 C360 40 420 180 410 290 C395 420 250 505 60 520 L0 520 Z" fill="var(--sky)"/>
    <path d="M200 0 C360 40 420 180 410 290" fill="none" stroke="var(--navy)" stroke-width="3"/>
    <path d="M300 543 C360 543 352 503 420 503 L768 503 L768 543 Z" fill="var(--navy)"/>
    <rect x="0" y="537" width="768" height="6" fill="var(--navy)"/>
  </svg>

  <ul class="features">
    <li><strong>Wide Variety of Sample Types:</strong>IRB-approved samples mimicking crime scene substances, including semen, hair, bone, saliva, blood, and vaginal epithelial cells.</li>
    <li><strong>Diverse Scenarios:</strong>Simulate sexual assault and degraded samples for varied conditions.</li>
    <li><strong>Custom Solutions:</strong>Tailored DNA quantities and concentrations to suit your lab's needs.</li>
  </ul>

  <div class="stamp" aria-label="Stamp area"></div>
  <div class="address-line" style="top:296px"></div>
  <div class="address-line" style="top:344px"></div>
  <div class="address-line" style="top:393px"></div>

  <p class="brand">Veltra Science</p>
  <p class="web">www.veltrascience.example</p>
</section>

</body>
</html>
```